Flyer Design Project for psychologist

I need an A4 flyer designed for a new psychology practice I am setting up called Brightpath Haven. The focus is to cater for the mental health and well-being of mums throughout their life stages, to help them live their best life whilst providing support and guidance in their journey through Motherhood.
The flyer will be used to promote the main services we provide and will echo the look and feel of website (www.brightpathhaven.com.au) and logo design. Images/photos can be downloaded off the Brightpath Haven website homepage slider or on "Our Services" page.
Corporate colours
Colours:
Bright green: Pantone 376
Bright green as CMYK: c: 45.2% m: 0% y: 100% k: 0%
Logo text large grey: 70% black
Logo text strapline: 75% black
Tree: 80% black
Fonts:
Logo 'Brightpath Haven': Verdana
Logo 'Counselling & coaching services for mums': Gill Sans Light
Updates
OMG you are all awesome!!!! Will be very very hard decision :-(
Target Market(s)
Mothers - all life stages wanting support counselling
Industry/Entity Type
Mental Health
Look and feel
Each slider illustrates characteristics of the customer's brand and the style your logo design should communicate.

```html
<!DOCTYPE html>
<html lang="en">
<head>
<meta charset="utf-8">
<title>Brightpath Haven – Counselling and Coaching for Mums</title>
<link rel="stylesheet" href="https://fonts.googleapis.com/css2?family=Lato:wght@300;400;700;900&family=Noto+Sans:wght@400;700&display=swap">
<style>
  :root {
    --green: #8dc21f;
    --grey-dark: #58585a;
    --grey-logo: #636365;
    --grey-text: #5a5a5c;
    --white: #ffffff;
    --sky-top: #2f6fc4;
    --sky-bottom: #8fbde8;
  }
  * { margin: 0; padding: 0; box-sizing: border-box; }
  html, body { width: 862px; height: 1200px; overflow: hidden; background: var(--white); }
  .flyer {
    position: relative;
    width: 862px;
    height: 1200px;
    font-family: "Lato", "Gill Sans", sans-serif;
    color: var(--grey-text);
  }
  .hero {
    height: 374px;
    background: linear-gradient(160deg, var(--sky-top) 0%, #4c8ad6 45%, var(--sky-bottom) 100%);
  }
  .title-band {
    height: 113px;
    background: var(--green);
    color: var(--white);
    padding: 21px 53px 0;
  }
  .title-band h1 {
    font-weight: 900;
    font-size: 30.5px;
    letter-spacing: 0.4px;
    line-height: 1.2;
  }
  .title-band p {
    font-weight: 300;
    font-size: 30px;
    line-height: 1.15;
  }
  .intro-band {
    height: 159px;
    background: var(--grey-dark);
    color: var(--white);
    padding: 29px 53px 0;
    font-size: 14.6px;
    line-height: 20.6px;
  }
  .services {
    padding: 25px 53px 0;
    height: 462px;
    position: relative;
  }
  .services-lead {
    font-weight: 300;
    font-size: 15px;
    margin-bottom: 9px;
  }
  .services-list {
    font-family: "Noto Sans", "Verdana", sans-serif;
    color: var(--green);
    font-size: 22.2px;
    line-height: 26px;
    letter-spacing: 0.1px;
    width: 770px;
  }
  .services-note {
    font-weight: 300;
    font-size: 15px;
    margin-top: 14px;
  }
  .brand {
    position: absolute;
    left: 53px;
    top: 318px;
  }
  .brand-name {
    font-family: "Noto Sans", "Verdana", sans-serif;
    font-weight: 700;
    font-size: 66px;
    line-height: 1;
    color: var(--grey-logo);
    letter-spacing: -0.5px;
  }
  .brand-tagline {
    font-weight: 300;
    font-size: 40px;
    line-height: 1;
    margin-top: 12px;
    color: var(--grey-dark);
  }
  .contact-band {
    height: 92px;
    background: var(--grey-dark);
    color: var(--white);
    display: flex;
    align-items: center;
    justify-content: center;
    font-family: "Noto Sans", "Verdana", sans-serif;
    font-size: 18.5px;
  }
  .contact-band .highlight { color: var(--green); font-size: 20px; margin: 0 5px; }
</style>
</head>
<body>
  <div class="flyer">
    <div class="hero" role="img" aria-label="Photo of a smiling mother and daughter with colourful balloons against a blue sky"></div>

    <header class="title-band">
      <h1>LIVE YOUR BEST LIFE WITH BRIGHTPATH HAVEN</h1>
      <p>COUNSELLING AND COACHING FOR MUMS</p>
    </header>

    <section class="intro-band">
      <p>Brightpath Haven provides counselling and coaching services especially for mums. Our main focus is to help you effectively deal with the daily issues that you may face that impacts on your mental health and wellbeing whilst providing support and guidance in your journey through Motherhood.<br>
      We help mums to uncover their strengths, set purposeful goals, develop the skills, ability and confidence that they need to be happier and lead meaningful and flourishing lives.</p>
    </section>

    <section class="services">
      <p class="services-lead">We can provide counselling and coaching for:</p>
      <p class="services-list">Non-Directive Pregnancy Support • Antenatal Depression • Preparing for Baby • Postnatal Depression • Anxiety • Motherhood Stress and Anger • Surviving and Thriving Through a Breakup • Work/Family Balance • Increasing Happiness • Finding Yourself in Motherhood</p>
      <p class="services-note">Medicare rebates are available for some services.</p>

      <div class="brand">
        <p class="brand-name">Brightpath Haven</p>
        <p class="brand-tagline">counselling &amp; coaching for mums</p>
      </div>
    </section>

    <footer class="contact-band">
      Call<span class="highlight">02 5550 1842</span>to make an appointment or visit<span class="highlight">www.brightpathhaven.com.au</span>
    </footer>
  </div>
</body>
</html>
```